Beautiful, sharp, website design for family-run property development company.

We are property developers in Kent (south east of London) who want to see the local town change. We are the only local property developer that is a family run business, focussing primarily on converting old, dilapidated Victorian buildings into beautiful residential spaces. Unlike other national developers, we work to regenerate buildings to create new employment opportunities, housing, and revive the town Centre .

Target Market(s)

1. Investors and Joint Venture partners - people with money to invest in property
2. Buyers of property - 25 to 40 year old, young professionals.
3. Commercial funders (people lending money to our projects
4. Professional team: Architects, builders, Estate agent who want to work with us

Industry/Entity Type

Real Estate Development

Coding

Number of Pages Required

Font styles to use
• Please follow the brief of stylish, elegant, modern

Colors

Designer to choose colors to be used in the design.

Requirements
Must have
• Please use these websites as a reference of what we are looking to achieve.
• http://brekmorestudio.com/#page5
• https://palvendro.co.uk/
• http://tamberfold.co.uk/
• http://www.thequarvishgroup.co.uk/about-quarvish
• Clean, simple, elegant, minimal design.
• Images of interiors of houses that have been converted from old buildings
• Images of farm buildings e.g. barns that have been converted to new homes or offices. Images of properties that may have been an old factory or old commercial property that is now a trendy apartment.
• Please use images of properties and interiors that are from the South East of England (including Kent, Surrey, Sussex, Hampshire, Dorset). There is a distinct style of housing in this part of England.
Nice to have
• Colours consistent with our brand colour palette (attached)

```html
<!DOCTYPE html>
<html lang="en">
<head>
<meta charset="utf-8">
<title>Larchmont Crest Property</title>
<link rel="stylesheet" href="https://fonts.googleapis.com/css2?family=Barlow+Condensed:wght@400;500;600&family=Montserrat:wght@200;300;500;800&family=Lato:ital,wght@0,300;0,400;1,300;1,400&family=Playfair+Display:wght@400&display=swap">
<style>
:root{
  --sage:#6e8c80;
  --sage-soft:#8fa89d;
  --mint-wash:#eef4ea;
  --mint-text:#eaf1e6;
  --ink:#1d1d1d;
  --muted:#8a9a94;
  --footer:#eef4f7;
  --ring:#e3eeec;
  --white:#ffffff;
}
*{margin:0;padding:0;box-sizing:border-box}
html,body{width:1200px;height:3537px;overflow:hidden;background:var(--white)}
body{position:relative;font-family:"Lato",sans-serif;color:var(--ink)}
.abs{position:absolute}
.photo{position:absolute}

/* sidebar */
.brand{left:30px;top:60px;width:186px;text-align:center;font-family:"Montserrat",sans-serif;font-weight:500;color:var(--sage);font-size:17px;letter-spacing:.5px;line-height:1.1}
.brand small{display:block;font-size:9px;letter-spacing:4px;margin-top:4px}
.brand-dot{display:block;width:40px;height:40px;border:1.5px solid var(--sage);border-radius:50%;margin:0 auto 12px}
.side-nav{left:32px;top:228px;list-style:none;font-family:"Barlow Condensed",sans-serif;font-weight:600;font-size:11px;line-height:23px;text-transform:uppercase;color:var(--ink)}
.side-contact{left:29px;top:476px;font-family:"Playfair Display",serif;font-size:9px;line-height:13px;color:var(--ink);font-style:normal}
.side-social{left:29px;top:563px;font-size:12px;color:var(--sage-soft)}

/* hero */
.hero{left:257px;top:0;width:943px;height:611px;
  background:
    radial-gradient(ellipse 260px 120px at 78% 18%,rgba(255,255,255,.75),rgba(255,255,255,0)),
    radial-gradient(ellipse 300px 110px at 30% 52%,rgba(255,255,255,.6),rgba(255,255,255,0)),
    radial-gradient(ellipse 220px 90px at 60% 40%,rgba(245,248,250,.55),rgba(255,255,255,0)),
    linear-gradient(90deg,rgba(0,0,0,0) 0%,rgba(0,0,0,0) 84%,rgba(120,72,36,.85) 88%,rgba(120,72,36,.85) 97%,rgba(0,0,0,0) 100%),
    linear-gradient(180deg,#7fb3d9 0%,#a9cde6 35%,#cfe0ea 55%,#a47a55 70%,#8a5630 82%,#5a3a24 100%)}
.hero-title{left:371px;top:162px;color:var(--white);line-height:1;font-family:"Montserrat",sans-serif}
.hero-title .l1{display:block;font-size:90px;font-weight:200;letter-spacing:1px}
.hero-title .l2{display:block;font-size:66px;font-weight:800;letter-spacing:0;margin-top:2px}
.hero-sub{left:640px;top:342px;width:322px;text-align:right;font-family:"Lato",sans-serif;font-weight:300;font-size:20px;color:var(--white)}
.hero-sub em{font-style:italic;font-weight:400}
.scroll{left:722px;top:482px;font-family:"Barlow Condensed",sans-serif;font-size:11px;color:var(--white);letter-spacing:.5px}

/* buildings */
.wash{left:257px;top:611px}
.big-word{font-family:"Montserrat",sans-serif;font-weight:800;color:var(--mint-text);letter-spacing:2px}
.bw-buildings{left:549px;top:630px;font-size:86px}
.sketch{left:880px;top:755px;width:320px;height:323px;background:linear-gradient(120deg,rgba(255,255,255,0) 0%,#f3f4f4 55%,#eceeee 100%)}
.spec-title{left:778px;top:760px;font-family:"Barlow Condensed",sans-serif;font-weight:500;font-size:27px;letter-spacing:.3px}
.rule{height:1px;width:33px;background:var(--sage-soft)}
.spec{left:778px;top:828px;list-style:none}
.spec li{height:48px}
.spec b{display:block;font-family:"Barlow Condensed",sans-serif;font-weight:500;font-size:11px;color:var(--sage);text-transform:uppercase}
.spec span{display:block;font-family:"Playfair Display",serif;font-size:8px;color:var(--muted);margin-top:4px}

/* features */
.feature{width:190px;text-align:center}
.feature svg{display:block;margin:0 auto}
.feature h3{font-family:"Barlow Condensed",sans-serif;font-weight:500;font-size:16px;margin-top:20px;letter-spacing:.3px}
.feature p{font-family:"Barlow Condensed",sans-serif;font-size:10.5px;color:var(--sage-soft);line-height:14px;margin:8px auto 0;width:130px}

/* video */
.video{left:257px;top:1443px;width:943px;height:442px;
  background:
    radial-gradient(ellipse 180px 140px at 88% 68%,rgba(70,90,96,.85),rgba(70,90,96,0)),
    radial-gradient(ellipse 330px 130px at 45% 80%,rgba(72,74,76,.9),rgba(72,74,76,0)),
    radial-gradient(ellipse 160px 100px at 20% 35%,rgba(248,248,248,.9),rgba(248,248,248,0)),
    linear-gradient(90deg,#6f6760 0%,#8e8b87 8%,#5f7a82 14%,#d9dcdc 30%,#eef0f0 55%,#e4e7e8 75%,#c8cbcc 100%)}

/* integrated */
.int-photo{left:257px;top:1961px;width:370px;height:424px;
  background:
    radial-gradient(ellipse 60px 120px at 48% 80%,rgba(92,140,90,.6),rgba(92,140,90,0)),
    radial-gradient(ellipse 70px 50px at 20% 88%,rgba(98,148,98,.55),rgba(98,148,98,0)),
    linear-gradient(90deg,#ededeb 0%,#f4f4f2 60%,#3a3a3a 70%,#efeeea 72%,#e9e6df 92%,#b9cfcd 100%)}
.int-title{left:680px;top:1985px;font-family:"Barlow Condensed",sans-serif;font-weight:500;font-size:27px}
.int-text{left:682px;top:2060px;width:270px;font-family:"Playfair Display",serif;font-size:10.5px;line-height:18px;color:var(--sage-soft)}
.int-sub{left:680px;top:2168px;font-family:"Barlow Condensed",sans-serif;font-weight:500;font-size:17px}
.rooms{left:680px;top:2218px;list-style:none;font-size:13.5px;line-height:27.5px}
.rooms .active{color:var(--sage-soft)}
.rooms .active i{display:inline-block;width:6px;height:6px;background:var(--sage);margin-right:22px;vertical-align:middle}

/* gallery */
.bw-gallery{left:257px;top:2495px;font-size:78px}
.gal-a{left:257px;top:2592px;width:333px;height:404px;
  background:
    radial-gradient(ellipse 70px 50px at 18% 78%,rgba(60,62,58,.85),rgba(60,62,58,0)),
    radial-gradient(ellipse 110px 90px at 35% 25%,rgba(104,140,84,.45),rgba(104,140,84,0)),
    linear-gradient(180deg,#f2f2ef 0%,#e6e7e2 65%,#d7d6d0 82%,#bdbbb4 100%)}
.gal-b{left:633px;top:2492px;width:332px;height:402px;
  background:
    radial-gradient(ellipse 40px 40px at 40% 44%,rgba(176,144,100,.9),rgba(176,144,100,0)),
    radial-gradient(ellipse 140px 50px at 45% 74%,rgba(200,184,160,.9),rgba(200,184,160,0)),
    linear-gradient(180deg,#eef0ee 0%,#c4dde1 20%,#bcd6db 55%,#e8e6e1 78%,#d9d6d0 100%)}
.caption{font-size:13px;line-height:17px}
.caption b{display:block;font-family:"Barlow Condensed",sans-serif;font-weight:500;font-size:13px}
.caption span{font-family:"Playfair Display",serif}
.caption strong{font-family:"Lato",sans-serif;font-weight:400}

/* strip */
.strip{left:257px;top:3143px;width:943px;height:188px;display:flex}
.strip div{flex:1}

/* footer */
.footer{left:257px;top:3331px;width:943px;height:206px;background:var(--footer)}
.f-title{left:287px;top:3376px;font-family:"Barlow Condensed",sans-serif;font-weight:400;font-size:15px;letter-spacing:1.5px;text-transform:uppercase}
.f-input{left:287px;top:3420px;width:482px;border-bottom:1px solid #c9d3d7;font-family:"Playfair Display",serif;font-size:8px;padding-bottom:4px;color:#555}
.f-btn{left:287px;top:3459px;width:96px;height:24px;border:1px solid #d2dadd;font-family:"Playfair Display",serif;font-size:8px;line-height:22px;padding-left:20px;color:#444}
.f-divider{left:802px;top:3358px;width:1px;height:165px;background:#c9d3d7}
.f-connect{left:849px;top:3373px;font-family:"Barlow Condensed",sans-serif;font-weight:400;font-size:12px;letter-spacing:1.5px;text-transform:uppercase}
.net{width:50px;text-align:center;font-family:"Playfair Display",serif;font-size:8px;color:#444}
.net i{display:block;width:8px;height:8px;border-radius:50%;background:var(--ink);margin:0 auto 8px}
</style>
</head>
<body>

<!-- sidebar -->
<div class="abs brand"><span class="brand-dot"></span>LARCHMONT CREST<small>PROPERTY</small></div>
<ul class="abs side-nav">
  <li>Investment</li><li>Gallery</li><li>Specification</li><li>Proerpty Plans</li><li>Contact Us</li>
</ul>
<address class="abs side-contact">hello@larchmontcrest.com<br>27 Harrow Mill Lane<br>Ashford 8011</address>
<div class="abs side-social">fo — ch — pb</div>

<!-- hero -->
<div class="photo hero" role="img" aria-label="City skyline with gothic towers and a clock tower under a cloudy blue sky"></div>
<h1 class="abs hero-title"><span class="l1">LARCHMONT</span><span class="l2">CREST PROPERTY</span></h1>
<p class="abs hero-sub">Property With <em>43 Appartments</em></p>
<div class="abs scroll">SCROLL DOWN</div>

<!-- buildings -->
<svg class="abs wash" width="354" height="498" viewBox="0 0 354 498"><polygon points="0,0 354,0 0,498" fill="var(--mint-wash)"/></svg>
<div class="abs big-word bw-buildings">BUILDINGS</div>
<div class="photo sketch" role="img" aria-label="Faint line sketch of a street of terraced buildings"></div>
<div class="photo" style="left:295px;top:776px;width:389px;height:248px;background:radial-gradient(ellipse 120px 70px at 50% 62%,rgba(170,168,164,.8),rgba(170,168,164,0)),linear-gradient(90deg,#e6e7e5 0%,#c9c7c1 30%,#8f857a 55%,#a5805f 100%),linear-gradient(180deg,#e2e5e8,#6d6862)" role="img" aria-label="Pedestrian high street lined with shops and hanging lights"></div>
<div class="photo" style="left:534px;top:750px;width:184px;height:250px;background:radial-gradient(ellipse 40px 60px at 62% 20%,rgba(140,175,210,.9),rgba(140,175,210,0)),linear-gradient(180deg,#a8744a 0%,#b48657 40%,#7a6048 62%,#4d5c6a 80%,#2f3c48 100%)" role="img" aria-label="Narrow old town street with ochre facades and wet paving"></div>
<h2 class="abs spec-title">751 MARROW STREET</h2>
<div class="abs rule" style="left:778px;top:813px"></div>
<ul class="abs spec">
  <li><b>Property size:</b><span>700sq ft</span></li>
  <li><b>Structure:</b><span>2 bedrooms</span></li>
  <li><b>Accommodation:</b><span>Furnished</span></li>
  <li><b>Heating:</b><span>Floor Heating</span></li>
</ul>

<!-- features -->
<div class="abs feature" style="left:269px;top:1138px">
  <svg width="140" height="140" viewBox="0 0 140 140"><circle cx="70" cy="70" r="64" fill="none" stroke="var(--ring)" stroke-width="2"/><path d="M70 6 A64 64 0 0 1 70 134" fill="none" stroke="#6f7a78" stroke-width="1.3"/>
  <g fill="none" stroke="var(--sage)" stroke-width="2"><path d="M52 72 L70 56 L88 72"/><path d="M57 68 V86 H72"/><circle cx="78" cy="79" r="6"/><path d="M82 83 L88 89"/></g></svg>
  <h3>BROWSE</h3><p>Proin gravida nibh vel velit auctor aluet nus mas gravida.</p>
</div>
<div class="abs feature" style="left:438px;top:1138px">
  <svg width="140" height="140" viewBox="0 0 140 140"><circle cx="70" cy="70" r="64" fill="none" stroke="var(--ring)" stroke-width="2"/><path d="M70 6 A64 64 0 0 1 70 134" fill="none" stroke="#6f7a78" stroke-width="1.3"/>
  <g fill="none" stroke="var(--sage)" stroke-width="2"><path d="M56 52 H78 L84 58 V72"/><path d="M56 52 V88 H70"/><path d="M61 62 H75 M61 70 H73 M61 78 H68"/><path d="M72 84 L81 76 L90 84 M75 81 V90 H87 V81"/></g></svg>
  <h3>INVEST</h3><p>Proin gravida nibh vel velit auctor aluet nus mas gravida.</p>
</div>
<div class="abs feature" style="left:607px;top:1138px">
  <svg width="140" height="140" viewBox="0 0 140 140"><circle cx="70" cy="70" r="64" fill="none" stroke="var(--ring)" stroke-width="2"/><path d="M70 6 A64 64 0 0 1 70 134" fill="none" stroke="#6f7a78" stroke-width="1.3"/>
  <g fill="none" stroke="var(--sage)" stroke-width="2"><path d="M70 48 V74"/><path d="M76 54 H67 a4 4 0 0 0 0 8 h6 a4 4 0 0 1 0 8 h-9"/><path d="M58 76 H82 L79 90 H61 Z"/></g></svg>
  <h3>PROPERTY</h3><p>Proin gravida nibh vel velit auctor aluet nus mas gravida.</p>
</div>
<div class="abs feature" style="left:776px;top:1138px">
  <svg width="140" height="140" viewBox="0 0 140 140"><circle cx="70" cy="70" r="64" fill="none" stroke="var(--ring)" stroke-width="2"/><path d="M70 6 A64 64 0 0 1 70 134" fill="none" stroke="#6f7a78" stroke-width="1.3"/>
  <g fill="none" stroke="var(--sage)" stroke-width="2"><rect x="54" y="50" width="32" height="40"/><path d="M54 57 H86"/><path d="M66 50 V62 L70 59 L74 62 V50"/></g>
  <text x="70" y="80" text-anchor="middle" font-family="Barlow Condensed, sans-serif" font-size="11" fill="var(--sage)">GDPR</text></svg>
  <h3>REGULATION</h3><p>Proin gravida nibh vel velit auctor aluet nus mas gravida.</p>
</div>

<!-- video -->
<div class="photo video" role="img" aria-label="Bright apartment bedroom with grey bedding, laptop, glass table and armchair by a window"></div>
<svg class="abs" style="left:684px;top:1620px" width="88" height="88" viewBox="0 0 88 88"><circle cx="44" cy="44" r="42" fill="none" stroke="#ffffff" stroke-width="1.5"/><polygon points="39,36 51,44 39,52" fill="#ffffff"/></svg>

<!-- integrated -->
<div class="photo int-photo" role="img" aria-label="White living room corner with black shelving, books and potted plants"></div>
<h2 class="abs int-title">INTEGRATED SOLUTIONS</h2>
<div class="abs rule" style="left:682px;top:2035px"></div>
<p class="abs int-text">Lorem ipsum dolor sit amet, consectetur adipisicing elit, do eius mod tempor incididunt ut labore et dolore magna aliqua. Ut enim ad min im veniam.</p>
<h3 class="abs int-sub">MUDOX RESIDENT FIRST FLOOR</h3>
<ul class="abs rooms">
  <li class="active"><i></i>Bedroom</li><li>Kids Room</li><li>Living Room</li><li>Office Room</li>
</ul>

<!-- gallery -->
<div class="abs big-word bw-gallery">GALLERY</div>
<div class="photo gal-b" role="img" aria-label="Pale blue arched wall with wooden sofa, cushions and woven pendant lamp"></div>
<div class="photo gal-a" role="img" aria-label="Sunlit room with black window frame, wire chair, throw and plants"></div>
<div class="abs caption" style="left:633px;top:2917px"><b>CALEDON, ON</b><span>Designer: </span><strong>Elena Varrow</strong></div>
<div class="abs caption" style="left:257px;top:3019px"><b>CALEDON, ON</b><span>Designer: </span><strong>Elena Varrow</strong></div>

<!-- strip -->
<div class="abs strip">
  <div role="img" aria-label="Relaxed resident leaning on a wooden chair" style="background:linear-gradient(135deg,#f1ebe6 0%,#e4c2bb 50%,#c9a27e 100%)"></div>
  <div role="img" aria-label="Modern villa with pool and timber deck" style="background:linear-gradient(180deg,#7fb8dc 0%,#e9e6df 40%,#6fb4c9 65%,#9c7c5c 100%)"></div>
  <div role="img" aria-label="White kitchen with brass pendant lamps" style="background:linear-gradient(180deg,#f3f2ef 0%,#ece9e3 60%,#d9cbb2 100%)"></div>
  <div role="img" aria-label="Dining chairs with green leaf cushion" style="background:linear-gradient(160deg,#ecebe7 0%,#d7c3a6 55%,#4f8a6c 80%,#b8956c 100%)"></div>
  <div role="img" aria-label="Glass towers against a teal sky" style="background:linear-gradient(180deg,#a3cacd 0%,#8fbabe 60%,#6e9da2 100%)"></div>
</div>

<!-- footer -->
<div class="abs footer"></div>
<h4 class="abs f-title">Subscribe to our newsletter</h4>
<div class="abs f-input">Your e-mail...</div>
<div class="abs f-btn">
  <svg class="abs" style="left:8px;top:8px" width="8" height="6" viewBox="0 0 8 6"><rect width="8" height="6" fill="#222"/><path d="M0 0 L4 3 L8 0" stroke="#fff" fill="none" stroke-width=".8"/></svg>Subscribe</div>
<div class="abs f-divider"></div>
<h4 class="abs f-connect">Connect with us</h4>
<div class="abs net" style="left:839px;top:3410px"><i></i>Folio</div>
<div class="abs net" style="left:892px;top:3410px"><i></i>Chirper</div>
<div class="abs net" style="left:839px;top:3451px"><i></i>Pinboard</div>
<div class="abs net" style="left:892px;top:3451px"><i></i>Reelhub</div>

</body>
</html>
```